Thornvale plumbing business cards

Want a functional designed for my business cards using my logo

Company Name- Thornvale Plumbing, Heating & Water Systems
Name- Martin Thornvale
Title- Vice President
Cell- 555-318-7742
Email- Thornvaleplumbing@mailbrook.example
Business address-
PO Box 57
Alderbrook, PA 21990

Plumbing

```html
<!DOCTYPE html>
<html lang="en">
<head>
<meta charset="utf-8">
<title>Thornvale Plumbing – Business Cards</title>
<link rel="stylesheet" href="https://fonts.googleapis.com/css2?family=Open+Sans:wght@300;400;700&family=Source+Sans+3:wght@400&display=swap">
<style>
  :root {
    --page-bg: #e6e6e6;
    --silver-light: #f4f4f4;
    --silver-dark: #d2d2d2;
    --panel-dark: #4f4f4f;
    --panel-mid: #5e5e5e;
    --accent-blue: #36b2e6;
    --card-blue: #3ab0e2;
    --card-blue-deep: #2fa3d6;
    --ink-grey: #4a4a4a;
    --ink-white: #ffffff;
  }
  * { box-sizing: border-box; margin: 0; padding: 0; }
  html, body { width: 1200px; height: 900px; overflow: hidden; }
  body {
    background: var(--page-bg);
    position: relative;
    font-family: "Open Sans", Arial, sans-serif;
  }
  .card {
    position: absolute;
    top: 324px;
    width: 440px;
    height: 251px;
    overflow: hidden;
  }
  .card--front { left: 130px; }
  .card--back { left: 630px; }

  .card__art { position: absolute; inset: 0; width: 100%; height: 100%; }

  .front__brand {
    position: absolute;
    left: 22px; top: 30px;
    font-size: 14px;
    font-weight: 400;
    color: var(--ink-grey);
  }
  .front__name {
    position: absolute;
    left: 22px; top: 66px;
    font-size: 14px;
    color: var(--ink-grey);
    white-space: nowrap;
  }
  .front__name-first { font-weight: 300; }
  .front__name-last { font-weight: 700; }
  .front__title {
    position: absolute;
    left: 22px; top: 86px;
    font-size: 9.5px;
    color: var(--ink-grey);
    letter-spacing: 0.2px;
  }
  .front__contact {
    position: absolute;
    right: 33px; top: 140px;
    text-align: right;
    color: var(--accent-blue);
    font-size: 12.5px;
    line-height: 17px;
  }
  .front__address { margin-top: 17px; }

  .back__photo { position: absolute; inset: 0; background: linear-gradient(135deg, var(--card-blue) 0%, var(--card-blue-deep) 100%); }
  .back__content {
    position: absolute;
    left: 0; right: 0; top: 118px;
    text-align: center;
    font-family: "Source Sans 3", Arial, sans-serif;
  }
  .back__brand { font-size: 29px; color: var(--ink-white); line-height: 1; }
  .back__tagline { font-size: 17px; color: var(--ink-white); margin-top: 4px; }
  .back__phone { font-size: 25px; color: var(--ink-grey); margin-top: 10px; }
</style>
</head>
<body>
  <section class="card card--front">
    <svg class="card__art" viewBox="0 0 722 412" preserveAspectRatio="none" aria-hidden="true">
      <defs>
        <linearGradient id="silver" x1="0" y1="0" x2="1" y2="1">
          <stop offset="0" stop-color="var(--silver-light)"/>
          <stop offset="1" stop-color="var(--silver-dark)"/>
        </linearGradient>
        <linearGradient id="panel" x1="0" y1="0" x2="1" y2="1">
          <stop offset="0" stop-color="var(--panel-mid)"/>
          <stop offset="1" stop-color="var(--panel-dark)"/>
        </linearGradient>
      </defs>
      <rect class="front__silver" width="722" height="412" fill="url(#silver)"/>
      <path class="front__accent-curve" d="M454 0 C330 40 240 200 176 412 L722 412 L722 0 Z" fill="var(--accent-blue)"/>
      <path class="front__dark-panel" d="M475 0 C360 50 270 210 203 412 L722 412 L722 0 Z" fill="url(#panel)"/>
    </svg>
    <div class="front__brand">Thornvale Plumbing</div>
    <div class="front__name"><span class="front__name-first">MARTIN</span><span class="front__name-last">THORNVALE</span></div>
    <div class="front__title">VICE PRESIDENT</div>
    <div class="front__contact">
      <div class="front__phone">555.318.7742</div>
      <div class="front__email">thornvaleplumbing@mailbrook.example</div>
      <div class="front__address">
        <div>PO Box 57</div>
        <div>Alderbrook, PA 21990</div>
      </div>
    </div>
  </section>

  <section class="card card--back">
    <div class="back__photo" role="img" aria-label="Blue-tinted photo of plumbing blueprints and pipe fittings"></div>
    <div class="back__content">
      <div class="back__brand">Thornvale Plumbing</div>
      <div class="back__tagline">Heating &amp; Water Systems</div>
      <div class="back__phone">555.204.6613</div>
    </div>
  </section>
</body>
</html>
```